Flyer Design

I need a flyer as Iam starting a business which cleans Leather couches,sofas,chairs for residential and businesses.
We clean the interiors of automobiles and marine craft, boats large and small.
We would like to be able to get across the message that we are affordable, personal and reliable.
The Gold coast is our market and within this area there is a large amount of holiday apartments and houses which do experience high traffic to their living and dinning areas.

Target Market(s)

Target market Home,Apartment,Marine and Auto Owners

Industry/Entity Type

Residential

Requirements
Must have
• The flyer must have Company name which is BRIGHT HIDE CARE MOBILE NUMBER
0471932054
EMAIL marvtolk@quellnet.com
Colours would like bright Gold or green or Red eith black lettering very modern font
Nice to have
• I would like to keep it as simple and clean looking.but eye catching
Should not have
• Dont want the flyer to look like a Real Estate flyer or a pizza advertisement.

```html
<!DOCTYPE html>
<html lang="en">
<head>
<meta charset="utf-8">
<title>Bright Hide Care – Flyer</title>
<link href="https://fonts.googleapis.com/css2?family=Exo+2:wght@500;600;700;800&display=swap" rel="stylesheet">
<style>
  :root {
    --red: #e8202a;
    --red-soft: #f9c9cc;
    --ink: #1d1d1f;
    --paper: #ffffff;
    --stage: #e9e7e4;
    --sofa: #1b1b1b;
    --sofa-shadow: #d9d9d9;
    --photo-warm: #c9a67e;
    --photo-cool: #a9b4b8;
  }
  html, body {
    margin: 0;
    padding: 0;
    width: 1200px;
    height: 1135px;
    overflow: hidden;
    background: var(--stage);
    font-family: "Exo 2", Arial, sans-serif;
  }
  .flyer {
    position: absolute;
    left: 172px;
    top: 30px;
    width: 856px;
    height: 1075px;
    background: var(--paper);
    box-sizing: border-box;
    border: 2px solid var(--red);
    overflow: hidden;
  }
  .brand-name {
    position: absolute;
    left: 0;
    right: 0;
    top: 28px;
    margin: 0;
    text-align: center;
    font-size: 84px;
    font-weight: 800;
    letter-spacing: 1px;
    color: var(--red);
    line-height: 1;
  }
  .wave {
    position: absolute;
    left: 0;
    top: 40px;
    width: 856px;
    height: 340px;
  }
  .hero-photo {
    position: absolute;
    left: 52px;
    top: 298px;
    width: 764px;
    height: 316px;
    background: linear-gradient(180deg, var(--sofa) 0%, #2c2c2c 70%, var(--sofa-shadow) 100%);
    border-radius: 6px;
  }
  .service-strip {
    position: absolute;
    top: 646px;
    height: 136px;
  }
  .strip-bar {
    background: var(--red);
    width: 38px;
  }
  .strip-bar.left { left: 224px; }
  .strip-bar.right { left: 587px; }
  .service-photo {
    box-sizing: border-box;
    border: 3px solid #ddd;
    width: 142px;
  }
  .service-photo.sofa-care { left: 268px; background: linear-gradient(135deg, var(--photo-warm), #e6d3b8); }
  .service-photo.floor-care { left: 438px; background: linear-gradient(135deg, var(--photo-cool), #e1e5e6); }
  .headline {
    position: absolute;
    left: 0;
    right: 0;
    margin: 0;
    text-align: center;
    line-height: 1;
  }
  .headline.primary {
    top: 790px;
    font-size: 66px;
    font-weight: 600;
    color: var(--red);
  }
  .headline.secondary {
    top: 866px;
    font-size: 53px;
    font-weight: 600;
    color: var(--ink);
  }
  .tagline {
    position: absolute;
    left: 0;
    right: 0;
    top: 943px;
    margin: 0;
    text-align: center;
    font-size: 27px;
    font-weight: 600;
    color: var(--ink);
  }
  .contact-band {
    position: absolute;
    left: 0;
    right: 0;
    bottom: 0;
    height: 62px;
    background: var(--red);
    display: flex;
    align-items: center;
    color: var(--paper);
    font-size: 26px;
    font-weight: 600;
  }
  .contact-item {
    flex: 0 0 auto;
    text-align: center;
  }
  .contact-item.phone { width: 410px; }
  .contact-item.email { flex: 1; }
  .contact-divider {
    width: 3px;
    height: 62px;
    background: var(--paper);
  }
</style>
</head>
<body>
  <main class="flyer">
    <svg class="wave" viewBox="0 0 856 340" aria-hidden="true">
      <path d="M0 250 C120 150 260 170 420 200 C600 235 760 200 856 80 L856 120 C770 250 600 290 420 260 C260 230 110 240 0 340 Z" fill="var(--red-soft)"/>
      <path d="M0 200 C120 110 270 130 430 165 C610 205 770 170 856 30 L856 90 C770 220 610 260 430 235 C260 210 110 215 0 300 Z" fill="var(--red)"/>
    </svg>
    <h1 class="brand-name">BRIGHT HIDE CARE</h1>

    <div class="hero-photo" role="img" aria-label="Black leather sofa with two cushions"></div>

    <div class="service-strip strip-bar left"></div>
    <div class="service-strip service-photo sofa-care" role="img" aria-label="Technician cleaning a cream leather couch"></div>
    <div class="service-strip service-photo floor-care" role="img" aria-label="Carpet being cleaned with an extraction machine"></div>
    <div class="service-strip strip-bar right"></div>

    <h2 class="headline primary">Cleaning Services for</h2>
    <h2 class="headline secondary">Residential and Businesses</h2>
    <p class="tagline">We offer Experience services with the best prices in town.</p>

    <footer class="contact-band">
      <span class="contact-item phone">Telephone: 0471932054</span>
      <span class="contact-divider"></span>
      <span class="contact-item email">Email:marvtolk@quellnet.com</span>
    </footer>
  </main>
</body>
</html>
```